vQ CARELINE (Brochure Design)

i need a proffesional brochure made. we are a mobile medical service company providing mobile Arterial Blood Gases(ABG's). Respiratory & Ventilator Consultation services. Ventilator and Tracheostomy training courses. and mobile vaccine administration.

this is my first time making a brochure so any and all advice/guidance will be appreciated.

i am thinking prints will be 8.5 inches x 11 inches (TRI-FOLD and BI-FOLD)

i have uploaded my business card design and logo design for reference.
as this brochure project continues ill update needs of the project descriptions.

Introduction: At vq CARELINE, we're dedicated to enhancing healthcare services by providing exceptional mobile arterial blood gases, respiratory and ventilator consultation services. Our core values revolve around excellence, compassion and accessibility. We believe that every individual deserves the highest standard of care, and we're committed to delivering that through expert guidance and top-notch training courses. Your health is at the heart of what we do, and we're here to support you on your journey to better respiratory health.

Mobile Arterial Blood Gases : Our mobile Arterial Blood Gas service offers quick, on-the-spot analysis of pH, oxygen, and carbon dioxide levels in your the blood. This service enables rapid adjustments to treatment plans for more effective respiratory care.

Ventilator and Tracheostomy Training: Our ventilator and tracheostomy course empowers caregivers and healthcare professionals to manage ventilators and care for tracheostomy patients with expertise. This training enhances patient safety, treatment outcomes, and healthcare provider confidence. vQ Careline your choice for top-notch care, convenience, and peace of mind.

Respiratory Consulting: Our respiratory consulting services provide expert guidance and support for individuals with respiratory / ventilator concerns. Benefits include personalized treatment plans, better management of respiratory conditions, and improved overall lung health. vQ Careline is your trusted partner for a breath of fresh air.

Target Market(s)

Sub-Acute facilities, Pulmonary Clinics, Pulmonologists, Nurses, Caregivers, Hospice and homehealth companies.

Industry/Entity Type

Medical; Respiratory; Nursing

Requirements
Must have
• proffesional simple design.

```html
<!DOCTYPE html>
<html lang="en">
<head>
<meta charset="utf-8">
<title>vQ CARELINE – Tri-fold Brochure</title>
<link rel="stylesheet" href="https://fonts.googleapis.com/css2?family=Montserrat:ital,wght@0,400;0,500;0,600;0,700;1,700&display=swap">
<style>
  :root {
    --navy: #06266b;
    --deep: #0a3a96;
    --blue: #1565d8;
    --sky: #2d9be8;
    --green: #6fd45a;
    --teal: #2fb8b0;
    --white: #ffffff;
    --text: #eaf3ff;
  }
  * { margin: 0; padding: 0; box-sizing: border-box; }
  html, body { width: 1200px; height: 857px; overflow: hidden; background: #dfe6ef; }
  .brochure {
    position: relative;
    width: 1200px; height: 857px;
    overflow: hidden;
    font-family: "Montserrat", Arial, sans-serif;
    color: var(--text);
    background: linear-gradient(160deg, var(--navy) 0%, var(--deep) 35%, var(--blue) 70%, var(--sky) 100%);
  }
  .fold { position: absolute; top: 0; width: 1px; height: 857px; background: rgba(255,255,255,0.08); }
  .fold--one { left: 400px; }
  .fold--two { left: 800px; }
  .panel { position: absolute; top: 0; height: 857px; width: 400px; }
  .panel--left { left: 0; }
  .panel--middle { left: 400px; }
  .panel--right { left: 800px; }

  .brand {
    position: absolute;
    display: flex; align-items: center; gap: 10px;
    font-weight: 500; font-size: 27px; letter-spacing: 0.5px;
    white-space: nowrap;
  }
  .brand__mark { width: 34px; height: 34px; }
  .brand--boxed {
    left: 45px; top: 146px; width: 248px; height: 58px;
    padding-left: 10px;
    border: 2px solid rgba(255,255,255,0.85);
    border-left: none;
    color: var(--white);
  }
  .brand--boxed .brand__mark { background: var(--white); }
  .brand--light {
    left: 93px; top: 42px; height: 44px; padding: 0 12px;
    background: var(--white); color: var(--deep);
    font-size: 22px;
  }
  .brand--light .brand__mark { width: 26px; height: 26px; background: var(--deep); }

  .ribbon {
    position: absolute; left: 0; top: 366px;
    width: 328px; height: 60px;
    background: linear-gradient(90deg, var(--teal), #46d2c6);
    clip-path: polygon(0 0, 100% 0, 88% 100%, 0 100%);
    padding: 6px 0 0 52px;
  }
  .ribbon__name { font-weight: 700; font-style: italic; font-size: 23px; color: var(--white); }
  .ribbon__role { font-size: 12px; color: var(--white); margin-top: 1px; }

  .heading { font-weight: 500; font-size: 31px; line-height: 1.08; color: var(--white); }
  .heading .accent { color: var(--green); font-weight: 600; }
  .heading--center { text-align: center; }

  .body-copy {
    font-size: 13.2px; line-height: 17.6px;
    text-align: justify; hyphens: auto;
    color: var(--text);
  }

  .left-heading { position: absolute; left: 52px; top: 456px; }
  .left-copy { position: absolute; left: 52px; top: 557px; width: 328px; }
  .follow {
    position: absolute; left: 52px; top: 802px;
    display: flex; align-items: center; gap: 14px;
    font-size: 12.5px; font-weight: 700; letter-spacing: 2.5px; color: var(--white);
  }
  .follow__icons { display: flex; gap: 8px; margin-left: 10px; }
  .follow__dot { width: 17px; height: 17px; border-radius: 50%; background: var(--green); }

  .abg-heading { position: absolute; left: 0; width: 400px; top: 92px; }
  .abg-copy { position: absolute; left: 25px; width: 350px; top: 178px; }
  .training-heading { position: absolute; left: 0; width: 400px; top: 306px; }
  .training-copy { position: absolute; left: 25px; width: 350px; top: 433px; }

  .consult-heading { position: absolute; left: 0; width: 400px; top: 120px; }
  .consult-copy { position: absolute; left: 40px; width: 318px; top: 207px; }
  .consult-copy p + p { margin-top: 17.6px; }
  .info { position: absolute; left: 104px; top: 422px; }
  .info__label { font-size: 14px; font-weight: 700; letter-spacing: 0.5px; color: var(--white); }
  .info__url { font-size: 14.5px; font-weight: 600; font-style: italic; color: var(--green); margin-top: 3px; }

  .photo { position: absolute; }
</style>
</head>
<body>
<main class="brochure">
  <span class="fold fold--one"></span>
  <span class="fold fold--two"></span>

  <section class="panel panel--left">
    <svg class="photo" style="left:0;top:0" width="340" height="352" viewBox="0 0 340 352" role="img" aria-label="Photo of a gloved clinician drawing an arterial blood sample from a patient's wrist">
      <defs>
        <linearGradient id="syringePhoto" x1="0" y1="0" x2="1" y2="1">
          <stop offset="0" stop-color="#8a96c8"/>
          <stop offset="0.5" stop-color="#b9a59a"/>
          <stop offset="1" stop-color="#4a5f9c"/>
        </linearGradient>
      </defs>
      <polygon points="0,0 250,0 330,130 260,345 0,345" fill="url(#syringePhoto)"/>
      <polyline points="250,0 330,130 260,345 0,345" fill="none" stroke="#ffffff" stroke-width="3"/>
    </svg>
    <div class="brand brand--boxed"><span class="brand__mark"></span>vQ CARELINE</div>
    <div class="ribbon">
      <div class="ribbon__name">Maren Delacroix</div>
      <div class="ribbon__role">Director</div>
    </div>
    <h2 class="heading left-heading"><span class="accent">Health</span><br>Professionals</h2>
    <p class="body-copy left-copy">At vq CARELINE, we're dedicated to enhancing healthcare services by providing exceptional mobile arterial blood gases, respiratory and ventilator consultation services. Our core values revolve around excellence, compassion and accessibility. We believe that every individual deserves the highest standard of care, and we're committed to delivering that through expert guidance and top-notch training courses. Your health is at the heart of what we do, and we're here to support you on your journey to better respiratory health.</p>
    <div class="follow">FOLLOW US
      <div class="follow__icons"><span class="follow__dot"></span><span class="follow__dot"></span><span class="follow__dot"></span></div>
    </div>
  </section>

  <section class="panel panel--middle">
    <h2 class="heading heading--center abg-heading">Mobile Arterial<br><span class="accent">Blood Gases</span></h2>
    <p class="body-copy abg-copy">Our mobile Arterial Blood Gas service offers quick, on-the-spot analysis of pH, oxygen, and carbon dioxide levels in your the blood. This service enables rapid adjustments to treatment plans for more effective respiratory care.</p>
    <h2 class="heading heading--center training-heading">Ventilator and<br><span class="accent">Tracheostomy<br>Training</span></h2>
    <p class="body-copy training-copy">Our ventilator and tracheostomy course empowers caregivers and healthcare professionals to manage ventilators and care for tracheostomy patients with expertise. This training enhances patient safety, treatment outcomes, and healthcare provider confidence. vQ Careline your choice for top-notch care, convenience, and peace of mind.</p>
    <svg class="photo" style="left:95px;top:603px" width="280" height="254" viewBox="0 0 280 254" role="img" aria-label="Product photo of a portable ventilator unit">
      <defs>
        <linearGradient id="ventPhoto" x1="0" y1="0" x2="0" y2="1">
          <stop offset="0" stop-color="#5a5f86"/>
          <stop offset="0.12" stop-color="#e9ecef"/>
          <stop offset="1" stop-color="#c9ced4"/>
        </linearGradient>
      </defs>
      <rect x="0" y="0" width="280" height="254" rx="8" fill="url(#ventPhoto)"/>
    </svg>
  </section>

  <section class="panel panel--right">
    <div class="brand brand--light"><span class="brand__mark"></span>vQ CARELINE</div>
    <h2 class="heading heading--center consult-heading"><span class="accent">Respiratory</span><br>Consulting</h2>
    <div class="body-copy consult-copy">
      <p>Our respiratory consulting services provide expert guidance and support for individuals with respiratory / ventilator concerns.</p>
      <p>Benefits include personalized treatment plans, better management of respiratory conditions, and improved overall lung health. vQ Careline is your trusted partner for a breath of fresh air.</p>
    </div>
    <div class="info">
      <div class="info__label">MORE INFORMATION</div>
      <div class="info__url">vqcarelinegroup.com</div>
    </div>
    <svg class="photo" style="left:28px;top:548px" width="372" height="309" viewBox="0 0 372 309" role="img" aria-label="Photo of a patient resting in a hospital bed beside a ventilator">
      <defs>
        <linearGradient id="patientPhoto" x1="0" y1="0" x2="1" y2="1">
          <stop offset="0" stop-color="#dfe9f3"/>
          <stop offset="0.55" stop-color="#a9c4df"/>
          <stop offset="1" stop-color="#6f93bf"/>
        </linearGradient>
      </defs>
      <polygon points="120,4 372,4 372,309 0,309 0,190" fill="url(#patientPhoto)"/>
      <polyline points="372,4 120,4 0,190" fill="none" stroke="#ffffff" stroke-width="3"/>
    </svg>
  </section>
</main>
</body>
</html>
```